Kelvar Systems Website

Website design for our company: Kelvar Systems.
The website should look fresh and IT focused. Please have a look at http://www.kelvarsystems.net.au/ for our current design. We want something fresh and new, professional looking, in WordPress so we can easily make changes.

Industry/Entity Type

It Company

```html
<!DOCTYPE html>
<html lang="en">
<head>
<meta charset="utf-8">
<title>Kelvar Systems</title>
<link href="https://fonts.googleapis.com/css2?family=Open+Sans:wght@400;600;700;800&display=swap" rel="stylesheet">
<style>
:root{
  --green:#2eab4c;
  --green-dark:#1c8a3b;
  --green-light:#8fd9a0;
  --blue:#1f86cf;
  --blue-dark:#166aa8;
  --text:#555;
  --heading:#2a9a45;
  --line:#dcdcdc;
  --bg:#ffffff;
}
*{margin:0;padding:0;box-sizing:border-box}
html,body{width:889px;height:1200px;overflow:hidden;background:var(--bg)}
body{position:relative;font-family:"Open Sans",Arial,sans-serif;color:var(--text)}
.abs{position:absolute}

/* header */
.brand{left:24px;top:8px;display:flex;align-items:center;gap:8px}
.brand-dot{width:34px;height:34px;border-radius:50%;background:var(--green)}
.brand-name{font-size:13px;font-weight:700;color:var(--green-dark)}
.phone{right:0;top:0;width:150px;height:34px;background:var(--green);border-bottom-left-radius:14px;color:#fff;font-weight:700;font-size:15px;display:flex;align-items:center;justify-content:center;gap:6px}
.nav{right:0;top:46px;display:flex;z-index:3}
.nav a{display:block;padding:0 10px;height:34px;line-height:34px;color:#fff;font-size:12px;font-weight:600;text-decoration:none;background:var(--green-dark);border-left:1px solid rgba(255,255,255,.2)}
.nav a.active{background:#fff;color:var(--green-dark)}

/* hero */
.hero{left:0;top:46px;width:889px;height:380px}
.hero-art{right:60px;top:70px;width:330px;height:250px;border-radius:50%;background:radial-gradient(circle,#e7f6e9 0%,#b7e4c0 60%,rgba(150,210,160,0) 75%)}
.hero-title{left:42px;top:142px;width:420px;color:#fff;font-weight:800;font-size:26px;line-height:32px;text-transform:uppercase;letter-spacing:.3px}
.dots{left:402px;top:326px;display:flex;gap:8px}
.dots span{width:12px;height:12px;border-radius:50%;background:#fff;opacity:.9}
.dots span:first-child{background:var(--blue);opacity:1}

/* services */
.section-title{color:var(--heading);font-weight:700;font-size:20px}
.services-title{left:0;width:889px;top:404px;text-align:center}
.intro{left:70px;width:749px;top:450px;height:36px;border-top:1px solid var(--line);border-bottom:1px solid var(--line);font-size:11px;display:flex;align-items:center;justify-content:center;font-style:italic}
.services{left:40px;top:500px;width:809px;display:flex;justify-content:space-between}
.service{width:160px;text-align:center}
.service svg{display:block;margin:0 auto}
.service-label{margin-top:6px;font-size:12px;font-weight:700;color:var(--blue-dark);white-space:nowrap}
.divider{left:40px;top:738px;width:809px;height:1px;background:var(--line)}

/* welcome */
.welcome-title{left:40px;top:750px;font-size:18px}
.welcome-text{left:40px;top:786px;width:420px;font-size:11px;line-height:15px}
.welcome-text p{margin-bottom:10px}
.welcome-art{left:490px;top:760px;width:360px;height:180px;border-radius:50% 50% 8px 8px;background:radial-gradient(ellipse at 50% 60%,#f3f3f3 0%,#dfe9f2 55%,#ffffff 80%)}

/* remote support */
.remote{left:0;top:950px;width:889px;height:52px;background:linear-gradient(#2a93dc,var(--blue-dark));display:flex;align-items:center;padding:0 40px;gap:24px}
.remote-label{color:#fff;font-weight:800;font-size:18px}
.remote-input{width:360px;height:32px;background:#fff;border-radius:3px;font-size:13px;font-style:italic;color:#888;display:flex;align-items:center;padding-left:10px}
.remote-btn{margin-left:auto;height:32px;padding:0 18px;background:var(--green);color:#fff;font-weight:700;font-size:12px;display:flex;align-items:center;border-radius:3px}

/* bottom */
.testi-title{left:40px;top:1012px;font-size:18px}
.testi-box{left:40px;top:1042px;width:340px;height:116px;border:1px solid var(--line);background:#f6f6f6;padding:10px 10px;font-size:9px;line-height:13px}
.testi-box p{width:230px}
.testi-name{left:170px;top:1138px;font-size:9px;font-style:italic}
.testi-photo{left:290px;top:1072px;width:80px;height:76px;background:linear-gradient(#cfd6dd,#9aa6b1)}
.contact-title{left:420px;top:1012px;font-size:18px}
.contact-map{left:420px;top:1042px;width:190px;height:116px;background:linear-gradient(135deg,#eef0e8,#d9e2d2)}
.contact-list{left:625px;top:1044px;font-size:10px;line-height:13px}
.contact-list li{list-style:none;display:flex;gap:6px;align-items:flex-start;margin-bottom:5px}
.footer{left:0;top:1178px;width:889px;height:22px;background:#f2f2f2;border-top:3px solid var(--green);display:flex;align-items:center;justify-content:space-between;padding:0 40px;font-size:9px}
.footer nav a{color:var(--green-dark);text-decoration:none;margin-right:4px}
</style>
</head>
<body>

<header>
  <div class="abs brand"><span class="brand-dot"></span><span class="brand-name">Kelvar Systems</span></div>
  <div class="abs phone">
    <svg width="14" height="14" viewBox="0 0 24 24"><path fill="#fff" d="M6.6 10.8a15 15 0 006.6 6.6l2.2-2.2c.3-.3.7-.4 1-.2 1.1.4 2.3.6 3.6.6.6 0 1 .4 1 1V20c0 .6-.4 1-1 1A17 17 0 013 4c0-.6.4-1 1-1h3.5c.6 0 1 .4 1 1 0 1.3.2 2.5.6 3.6.1.3 0 .7-.2 1z"/></svg>
    088-410-5720
  </div>
  <nav class="abs nav">
    <a class="active" href="#">Home</a><a href="#">About</a><a href="#">Service</a><a href="#">Clients</a><a href="#">Supports</a><a href="#">Testimonials</a><a href="#">Contact</a>
  </nav>
</header>

<section class="abs hero">
  <svg class="abs" width="889" height="380" viewBox="0 0 889 380" style="left:0;top:0">
    <defs>
      <linearGradient id="heroGrad" x1="0" y1="0" x2="1" y2="1">
        <stop offset="0" stop-color="#1e9a44"/><stop offset=".6" stop-color="#35b556"/><stop offset="1" stop-color="#6acb7f"/>
      </linearGradient>
    </defs>
    <path d="M0 0H889V290C700 340 400 360 0 330Z" fill="url(#heroGrad)"/>
    <path d="M0 330C400 360 700 340 889 290V380H0Z" fill="#fff"/>
  </svg>
  <div class="abs hero-art" role="img" aria-label="Key in a circular maze illustration"></div>
  <h1 class="abs hero-title">To excel in the support and service of all computer and IT needs</h1>
  <div class="abs dots"><span></span><span></span><span></span><span></span></div>
</section>

<h2 class="abs section-title services-title">Our Services</h2>
<p class="abs intro">“ Kelvar Systems is an Adelaide based company with a single objective - to excel in the support and service of all computer and IT needs. ”</p>

<div class="abs services">
  <div class="service">
    <svg width="110" height="190" viewBox="0 0 110 190"><path d="M55 4a51 51 0 0151 51c0 38-51 96-51 96S4 93 4 55A51 51 0 0155 4z" fill="#2eab4c"/><circle cx="55" cy="55" r="40" fill="#fff"/><circle cx="55" cy="55" r="34" fill="#9fd3e8" role="img" aria-label="Technician icon"/><ellipse cx="55" cy="180" rx="22" ry="5" fill="#e2e2e2"/></svg>
    <div class="service-label">On-site Service</div>
  </div>
  <div class="service">
    <svg width="110" height="190" viewBox="0 0 110 190"><path d="M55 4a51 51 0 0151 51c0 38-51 96-51 96S4 93 4 55A51 51 0 0155 4z" fill="#1f86cf"/><circle cx="55" cy="55" r="40" fill="#fff"/><circle cx="55" cy="55" r="34" fill="#c9d4e0" role="img" aria-label="Server icon"/><ellipse cx="55" cy="180" rx="22" ry="5" fill="#e2e2e2"/></svg>
    <div class="service-label">Remote Desktop Support</div>
  </div>
  <div class="service">
    <svg width="110" height="190" viewBox="0 0 110 190"><path d="M55 4a51 51 0 0151 51c0 38-51 96-51 96S4 93 4 55A51 51 0 0155 4z" fill="#21a3b8"/><circle cx="55" cy="55" r="40" fill="#fff"/><circle cx="55" cy="55" r="34" fill="#d9e6ee" role="img" aria-label="Medical computer icon"/><ellipse cx="55" cy="180" rx="22" ry="5" fill="#e2e2e2"/></svg>
    <div class="service-label">Medical IT Service</div>
  </div>
  <div class="service">
    <svg width="110" height="190" viewBox="0 0 110 190"><path d="M55 4a51 51 0 0151 51c0 38-51 96-51 96S4 93 4 55A51 51 0 0155 4z" fill="#1f86cf"/><circle cx="55" cy="55" r="40" fill="#fff"/><circle cx="55" cy="55" r="34" fill="#b9d9f0" role="img" aria-label="Web design icon"/><ellipse cx="55" cy="180" rx="22" ry="5" fill="#e2e2e2"/></svg>
    <div class="service-label">Website Design</div>
  </div>
  <div class="service">
    <svg width="110" height="190" viewBox="0 0 110 190"><path d="M55 4a51 51 0 0151 51c0 38-51 96-51 96S4 93 4 55A51 51 0 0155 4z" fill="#2eab4c"/><circle cx="55" cy="55" r="40" fill="#fff"/><circle cx="55" cy="55" r="34" fill="#f0c9a0" role="img" aria-label="Disaster recovery icon"/><ellipse cx="55" cy="180" rx="22" ry="5" fill="#e2e2e2"/></svg>
    <div class="service-label">Disaster Recovery</div>
  </div>
</div>
<div class="abs divider"></div>

<h2 class="abs section-title welcome-title">WELCOME TO KELVAR SYSTEMS</h2>
<div class="abs welcome-text">
  <p>Kelvar Systems is an Adelaide based company with a single objective - to excel in the support and service of all computer and IT needs.</p>
  <p>We provide a high level of consulting services using the most experienced engineers at a reasonable and fair price. We believe in using a business value approach to every aspect of computer consulting to provide our clients with the most cost effective solutions.</p>
  <p>We strongly believe that we are in business with our clients. Each thing we do must be measured against our clients' business objectives. At the end of the day our client's success is our success.</p>
</div>
<div class="abs welcome-art" role="img" aria-label="Circle of colourful chairs illustration"></div>

<div class="abs remote">
  <span class="remote-label">REMOTE SUPPORT</span>
  <span class="remote-input">Enter your 6-digit code</span>
  <span class="remote-btn">CONNECT NOW</span>
</div>

<h2 class="abs section-title testi-title">Testimonials</h2>
<div class="abs testi-box"><p>Lorem ipsum dolor sit amet, consectetur adipiscing elit. Mauris ultricies orci quis nisl bibendum pharetra. Proin varius molestie tempus mauris. Fusce scelerisque luctus nunc.</p></div>
<div class="abs testi-photo" role="img" aria-label="Client photo"></div>
<span class="abs testi-name">Marcus Hale</span>

<h2 class="abs section-title contact-title">Contact</h2>
<div class="abs contact-map" role="img" aria-label="Location map"></div>
<ul class="abs contact-list">
  <li><svg width="10" height="12" viewBox="0 0 10 12"><path d="M5 0a4 4 0 014 4c0 3-4 8-4 8S1 7 1 4a4 4 0 014-4z" fill="#1c8a3b"/></svg><span>27 Harbour Lane,<br>Northfield 5085,<br>Australia</span></li>
  <li><svg width="10" height="10" viewBox="0 0 10 10"><rect width="10" height="10" rx="2" fill="#1c8a3b"/></svg><span>0884105720</span></li>
  <li><svg width="10" height="10" viewBox="0 0 10 10"><rect width="10" height="10" rx="2" fill="#1c8a3b"/></svg><span>0872051194</span></li>
  <li><svg width="10" height="10" viewBox="0 0 10 10"><rect width="10" height="10" rx="2" fill="#1c8a3b"/></svg><span>0884108863</span></li>
</ul>

<footer class="abs footer">
  <nav><a href="#">Home</a>| <a href="#">About</a>| <a href="#">Service</a>| <a href="#">Clients</a>| <a href="#">Supports</a>| <a href="#">Testimonials</a>| <a href="#">Contact</a></nav>
  <span>Copyright © 2014 Kelvar Systems Pty Ltd. All Rights Reserved.</span>
</footer>

</body>
</html>
```